Postcard Design

I am a mortgage broker located in Michigan. I recently opened my own company after working for another for 7 years. I want to send out a mailing letting my old clients know my new information and also reach out to them to let me know if I can assist them with anything.

Industry/Entity Type

It Company

```html
<!DOCTYPE html>
<html lang="en">
<head>
<meta charset="utf-8">
<title>Summit Lending Postcard</title>
<link href="https://fonts.googleapis.com/css2?family=Didact+Gothic&family=Mulish:wght@700&family=Signika:wght@600&display=swap" rel="stylesheet">
<style>
  :root {
    --brand-blue: #1b75bb;
    --accent-orange: #f07b22;
    --charcoal: #45403b;
    --navy-ink: #1d3f57;
    --body-ink: #2b2b2b;
    --white: #ffffff;
    --backdrop: #6f6f6f;
  }
  * { margin: 0; padding: 0; box-sizing: border-box; }
  html, body { width: 1200px; height: 1200px; overflow: hidden; }
  body { background: var(--backdrop); position: relative; font-family: "Didact Gothic", sans-serif; }

  .postcard { position: absolute; left: 252px; width: 698px; background: var(--white); overflow: hidden; box-shadow: 0 2px 6px rgba(0,0,0,.35); }
  .postcard--front { top: 36px; height: 540px; }
  .postcard--back { top: 608px; height: 542px; }
  .postcard svg.shapes { position: absolute; inset: 0; }

  /* Front */
  .front-header { position: absolute; left: 0; top: 0; width: 100%; height: 105px; background: var(--brand-blue); }
  .front-header__kicker { position: absolute; left: 60px; top: 33px; font-family: "Mulish", sans-serif; font-weight: 700; font-size: 14px; color: var(--white); }
  .front-header__headline { position: absolute; left: 60px; top: 50px; font-family: "Mulish", sans-serif; font-weight: 700; font-size: 37px; color: var(--white); letter-spacing: .2px; white-space: nowrap; }

  .brand-name { font-family: "Signika", sans-serif; font-weight: 600; font-size: 20px; letter-spacing: .3px; white-space: nowrap; }
  .front-brand { position: absolute; left: 0; width: 430px; top: 180px; text-align: center; color: var(--brand-blue); }
  .front-brand__rule { position: absolute; left: 84px; top: 218px; width: 196px; height: 1px; background: #8c8c8c; }

  .front-intro { position: absolute; left: 30px; top: 226px; width: 350px; font-size: 16px; line-height: 31.2px; color: var(--body-ink); }

  .contact-block { position: absolute; left: 0; top: 432px; width: 420px; height: 108px; text-align: center; color: var(--white); }
  .contact-block__phone { font-family: "Signika", sans-serif; font-weight: 600; font-size: 34px; letter-spacing: 1px; margin-top: 10px; }
  .contact-block__email { font-family: "Signika", sans-serif; font-weight: 600; font-size: 17px; letter-spacing: .4px; margin-top: 8px; }

  .signature { position: absolute; left: 440px; width: 228px; top: 452px; text-align: center; color: var(--navy-ink); font-family: "Signika", sans-serif; font-weight: 600; }
  .signature__name { font-size: 26px; letter-spacing: .6px; }
  .signature__title { font-size: 16px; margin-top: 2px; }

  /* Back */
  .back-brand { position: absolute; left: 0; width: 388px; top: 80px; text-align: center; color: var(--white); }
  .back-message { position: absolute; left: 0; width: 388px; top: 397px; text-align: center; font-size: 16.5px; line-height: 24px; color: var(--body-ink); }
</style>
</head>
<body>

<section class="postcard postcard--front">
  <svg class="shapes" width="698" height="540" viewBox="0 0 698 540">
    <defs>
      <linearGradient id="portraitTone" x1="0" y1="0" x2="1" y2="1">
        <stop offset="0" stop-color="#5a5450"/>
        <stop offset=".55" stop-color="#4a4642"/>
        <stop offset="1" stop-color="#2a3447"/>
      </linearGradient>
      <clipPath id="frontRightClip">
        <path d="M400 106 Q360 330 432 540 H698 V106 Z"/>
      </clipPath>
    </defs>
    <rect x="0" y="432" width="460" height="108" fill="var(--charcoal)"/>
    <g clip-path="url(#frontRightClip)">
      <rect x="340" y="106" width="358" height="326" fill="url(#portraitTone)" role="img" aria-label="Portrait photo of the company president in a suit and tie"/>
      <rect x="340" y="432" width="358" height="108" fill="var(--white)"/>
    </g>
    <path d="M400 106 Q360 330 432 540" fill="none" stroke="var(--accent-orange)" stroke-width="5"/>
    <rect x="0" y="105" width="698" height="2" fill="var(--white)"/>
  </svg>

  <header class="front-header">
    <p class="front-header__kicker">Welcome to the Loan Center!</p>
    <h1 class="front-header__headline">Are you looking to buy a home?</h1>
  </header>

  <div class="front-brand brand-name">SUMMIT LENDING</div>
  <div class="front-brand__rule"></div>

  <p class="front-intro">Summit Lending Group, LLC is committed to providing you with the best service, pricing, and programs to meet your mortgage needs. We are equipped to handle your Conventional and government purchase or refinance loan needs.</p>

  <div class="contact-block">
    <p class="contact-block__phone">248-555-0147</p>
    <p class="contact-block__email">DAN@SUMMITLENDINGGROUP</p>
  </div>

  <div class="signature">
    <p class="signature__name">DANIEL REYES</p>
    <p class="signature__title">PRESIDENT</p>
  </div>
</section>

<section class="postcard postcard--back">
  <svg class="shapes" width="698" height="542" viewBox="0 0 698 542">
    <defs>
      <linearGradient id="houseTone" x1="0" y1="0" x2="0" y2="1">
        <stop offset="0" stop-color="#a9cdee"/>
        <stop offset=".35" stop-color="#8a8580"/>
        <stop offset=".82" stop-color="#5d5753"/>
        <stop offset="1" stop-color="#4f8a3a"/>
      </linearGradient>
      <clipPath id="backLeftClip">
        <path d="M0 0 H365 Q468 271 345 542 H0 Z"/>
      </clipPath>
    </defs>
    <g clip-path="url(#backLeftClip)">
      <rect x="0" y="0" width="470" height="122" fill="var(--brand-blue)"/>
      <rect x="0" y="122" width="470" height="261" fill="url(#houseTone)" role="img" aria-label="Photo of a large two-story stone and stucco family home under a blue sky"/>
    </g>
    <path d="M368 0 Q470 271 348 542" fill="none" stroke="var(--brand-blue)" stroke-width="10"/>
  </svg>

  <div class="back-brand brand-name">SUMMIT LENDING</div>

  <p class="back-message">To learn more about applying for a mortgage<br>with Summit Lending Group, LLC<br>please call Daniel Reyes at<br>(248) 555-0147 or<br>dan@summitlendinggroup.com</p>
</section>

</body>
</html>
```